BUSINESS CARD for Tidal Fitness, upscale rowing studio

We need a business card design for a new company called Tidal Fitness, a boutique rowing studio. Our program offers high intensity workouts at low impact on the joints and body. We want clean, sleek designs that uses only our logo and information. The final design should communicate strength and class. Our slogan is Row for life.

Industry/Entity Type

Fitness

Contact Information for Business Card

Joan Perrick
Tidal Fitness
tidalfitnessmobile@examplemail.com
318.472.9016
www.tidal-fitness.example

Font styles to use
Sans Serif

Colors
0455a3
3276b5
85acd3
0592cd
32a6d6
85cae6

Requirements
Must have
• Must have:
• LOGO (provided) and business card details
Nice to have
• Want the design to be VERY SIMPLE. sleek. elegant. strong.
• might want to print on translucent cards
• would like to see some PORTRAIT designs.
Should not have
• should not have any extra drawings or art. do not use icons beside business card details information

```html
<!DOCTYPE html>
<html lang="en">
<head>
<meta charset="UTF-8">
<title>Tidal Fitness — Business Card</title>
<link href="https://fonts.googleapis.com/css2?family=Raleway:wght@300;400;500&display=swap" rel="stylesheet">
<style>
  :root {
    --page: #ffffff;
    --card-dark: #23272e;
    --brand-blue: #3276b5;
    --brand-deep: #0455a3;
    --brand-sky: #85acd3;
    --accent: #0592cd;
    --text-light: #e9eef5;
    --text-muted: #b9c4d2;
  }
  * { margin: 0; padding: 0; box-sizing: border-box; }
  html, body { width: 876px; height: 1200px; overflow: hidden; background: var(--page); }
  body { position: relative; font-family: "Raleway", sans-serif; }

  .card { position: absolute; border-radius: 16px; overflow: hidden; box-shadow: 0 2px 6px rgba(0,0,0,0.12); }

  /* Front card */
  .card-front { left: 205px; top: 302px; width: 475px; height: 298px; background: var(--card-dark); }
  .front-panel {
    position: absolute; left: 52px; top: 0; width: 181px; height: 100%;
    background: linear-gradient(180deg, #3c80bf 0%, var(--brand-blue) 55%, #2a69a6 100%);
  }
  .front-brand {
    position: absolute; left: 52px; top: 120px; width: 181px; text-align: center; color: #fff;
  }
  .brand-dot { width: 30px; height: 30px; border: 2px solid #fff; border-radius: 50%; margin: 0 auto 12px; }
  .brand-name { font-weight: 400; font-size: 14px; letter-spacing: 2.5px; white-space: nowrap; }

  .contact { position: absolute; right: 80px; top: 72px; text-align: right; color: var(--text-light); font-weight: 300; }
  .contact-name { font-size: 15px; font-weight: 400; }
  .contact-role { font-size: 8px; color: var(--text-muted); margin-top: 2px; }
  .contact-line { font-size: 9.5px; margin-top: 22px; line-height: 1.35; white-space: nowrap; }

  .name-bar { position: absolute; right: 0; top: 82px; width: 62px; height: 7px; background: var(--accent); }

  /* Back card */
  .card-back {
    left: 219px; top: 650px; width: 465px; height: 287px;
    background: linear-gradient(160deg, #4a8cc8 0%, var(--brand-blue) 50%, #2c6fae 100%);
  }
  .back-brand { position: absolute; left: 0; top: 84px; width: 100%; text-align: center; color: #fff; }
  .back-brand .brand-dot { width: 54px; height: 54px; border-width: 3px; margin-bottom: 14px; }
  .back-brand .brand-name { font-size: 22px; letter-spacing: 5px; }
  .slogan { margin-top: 10px; font-size: 10px; font-weight: 300; letter-spacing: 3px; color: var(--text-light); }
</style>
</head>
<body>
  <section class="card card-front">
    <div class="front-panel" role="img" aria-label="Soft blue photo of rowers in the studio"></div>
    <div class="front-brand">
      <div class="brand-dot"></div>
      <div class="brand-name">TIDAL FITNESS</div>
    </div>

    <div class="contact">
      <div class="contact-name">Joan Perrick</div>
      <div class="contact-role">manager</div>
      <div class="contact-line">tidalfitnessmobile@examplemail.com</div>
      <div class="contact-line">Harbor Road 214,<br>Bay City</div>
      <div class="contact-line">318.472.9016<br>www.tidal-fitness.example</div>
    </div>

    <div class="name-bar"></div>
  </section>

  <section class="card card-back" role="img" aria-label="Soft blue photo of people rowing on the water">
    <div class="back-brand">
      <div class="brand-dot"></div>
      <div class="brand-name">TIDAL FITNESS</div>
      <div class="slogan">ROW FOR LIFE</div>
    </div>
  </section>
</body>
</html>
```